London Based Property Finding Company - have logo already

We find property for private purchasers and investors in London, UK.  We work for the BUYER, whereas estate agencies/real estate companies work for the seller. We offer a much more personalised service to UK and overseas purchasers.

We would like the following:

*A double sided business card

*A letterhead

We have attached two versions of the logo. Each logo style is set on two different coloured backgrounds. Please choose one of the two designs, whichever you prefer or feel more comfortable with, and produce one in black and one in white background.

This applies to both pieces of stationery.

THE BUSINESS CARD:

We would like the company name placed on its own on one side of the card and the contact details and what we do on the other.

e.g.

SIDE 1:

BRAMWELL PROPERTY FINDERS

SIDE 2:

Owen Bramwell

t: 0208 394 2860

m: +44(0)7932 418 507

e: info@bramwellpropertyfinders.co.uk

w: bramwellpropertyfinders.co.uk

London Property Finders and Search Agents

I will leave the layout up to you, but a minimalist layout is preferred. If you would like to put additional detial or design on the card then that is up to, but not specified.

It is optional to have the company name on side 2, but if you do use it, please make it smaller. than on the 1st side.

The design needs to be simple, professional and not too in your face.

If you are using the black background design on side 1 for the logo, then maybe a white backgounnd can be used on side 2 with a black typeface.

The type face for the contacts details should be sans serif standard typeface. Please experiment with the desciprtion.

-

THE LETTERHEAD;

You can experiment with the layout for the letterhead. e.g logo centre aligned on the top of the page with the contact details and address at the bottom of the page OR the logo, description running along a bar on the top of the page with the contact details and website address at the bottom. Please try and experiment with this, but the less 'busy', the better.

Here is info that needs to be on the letterhead.

Bramwell Property Finders

t: 0208 394 2860

m: +44(0)7932 418 507

(PLEASE NOTE; the below company info must be placed at the bottom of the page as a footer, in small text.)

Kestrand Holdings Ltd Trading as Bramwell Property Finders, a company registered in England & Wales, No.7351926 , Registered office is 41 Hollinmoor Court, Hollinmoor Road, London, SW9 3PL, t: 0208 394 2860, m: +44(0)7932 418 507, e: info@bramwellpropertyfinders.co.uk

Best of luck!

Thank you

Dear Designer,

I have now attached the supporting files to this brief.

Thanks,

Owen Bramwell
Bramwell Property Finders

```html
<!DOCTYPE html>
<html lang="en">
<head>
<meta charset="utf-8">
<title>Bramwell Property Finders – Stationery</title>
<link rel="stylesheet" href="https://fonts.googleapis.com/css2?family=Lato:wght@300;400;700;900&display=swap">
<style>
  :root {
    --ink: #000000;
    --text: #222222;
    --paper: #ffffff;
    --accent: #7fe3f2;
    --accent-faint: rgba(127, 227, 242, 0.10);
    --frame: #9a9a9a;
    --page-bg: #ffffff;
  }
  * { box-sizing: border-box; margin: 0; padding: 0; }
  html, body {
    width: 1200px; height: 1178px; overflow: hidden;
    background: var(--page-bg);
    font-family: "Lato", "Helvetica Neue", Arial, sans-serif;
    color: var(--text);
  }
  .canvas { position: relative; width: 1200px; height: 1178px; }

  .label { color: var(--accent); font-weight: 700; }

  /* Wordmark stand-in */
  .wordmark {
    color: var(--paper);
    font-weight: 400;
    text-transform: uppercase;
    letter-spacing: 0.04em;
    white-space: nowrap;
  }

  /* Letterhead */
  .letterhead {
    position: absolute; left: 19px; top: 15px;
    width: 806px; height: 1141px;
    background: var(--paper);
    border: 1px solid var(--frame);
    overflow: hidden;
  }
  .letterhead__header {
    height: 116px; background: var(--ink);
    display: flex; align-items: center; padding-left: 30px;
  }
  .letterhead__header .wordmark { font-size: 28px; }
  .letterhead__rule { height: 10px; background: var(--accent); }
  .letterhead__contact {
    position: absolute; right: 26px; top: 134px;
    text-align: right; font-size: 14px; line-height: 24px; font-weight: 300;
    white-space: nowrap;
  }
  .letterhead__contact .company { font-weight: 700; margin-right: 14px; }
  .sep { margin: 0 6px; }
  .letterhead__motif {
    position: absolute; left: 218px; top: 391px;
    width: 587px; height: 684px;
    background: radial-gradient(circle at 40% 35%, var(--accent-faint) 0%, rgba(127,227,242,0.04) 45%, rgba(255,255,255,0) 70%);
  }
  .letterhead__footer {
    position: absolute; left: 22px; bottom: 24px;
    font-size: 8.6px; line-height: 15px; font-weight: 300;
    white-space: nowrap;
  }
  .letterhead__footer-rule {
    position: absolute; left: 0; right: 0; bottom: 0;
    height: 11px; background: var(--accent);
  }

  /* Business cards */
  .card {
    position: absolute; left: 850px; width: 326px;
    overflow: hidden;
  }
  .card--front {
    top: 23px; height: 210px; background: var(--ink);
    display: flex; align-items: center; padding-left: 22px;
  }
  .card--front .wordmark { position: relative; font-size: 15px; }
  .card__motif {
    position: absolute; right: -20px; top: 20px;
    width: 170px; height: 190px;
    background: radial-gradient(circle at 45% 40%, rgba(255,255,255,0.07) 0%, rgba(255,255,255,0) 65%);
  }
  .card--back {
    top: 271px; height: 213px; background: var(--paper);
    border: 1px solid var(--frame);
  }
  .card--back .card__motif {
    top: 10px; right: -30px;
    background: radial-gradient(circle at 45% 40%, var(--accent-faint) 0%, rgba(255,255,255,0) 65%);
  }
  .card__details {
    position: absolute; left: 24px; top: 44px;
    font-size: 12.5px; font-weight: 300;
    white-space: nowrap;
  }
  .card__name { font-size: 20px; font-weight: 900; letter-spacing: 0.02em; margin-bottom: 4px; }
  .card__line { line-height: 23px; }
  .card__line--web { margin-top: 8px; }
  .card__rule {
    position: absolute; left: 0; right: 0; bottom: 29px;
    height: 4px; background: var(--accent);
  }
  .card__tagline {
    position: absolute; left: 0; right: 0; bottom: 0; height: 29px;
    background: var(--ink); color: var(--paper);
    font-size: 13px; font-weight: 300;
    display: flex; align-items: center; padding-left: 14px;
  }
</style>
</head>
<body>
<div class="canvas">

  <section class="letterhead">
    <header class="letterhead__header">
      <span class="wordmark">Bramwell Property Finders</span>
    </header>
    <div class="letterhead__rule"></div>

    <div class="letterhead__contact">
      <div><span class="company">Bramwell Property Finders</span><span class="label">T:</span> 0208 394 2860<span class="sep">|</span><span class="label">M:</span> +44(0)7932 418 507</div>
      <div><span class="label">E:</span> info@bramwellpropertyfinders.co.uk<span class="sep">|</span><span class="label">W:</span> bramwellpropertyfinders.co.uk</div>
    </div>

    <div class="letterhead__motif" role="img" aria-label="Faint outline of a large magnifying glass as a background motif"></div>

    <footer class="letterhead__footer">
      <div><span class="label">T:</span> 0208 394 2860<span class="sep">|</span><span class="label">M:</span> +44(0)7932 418 507<span class="sep">|</span><span class="label">E:</span> info@bramwellpropertyfinders.co.uk</div>
      <div>Kestrand Holdings Ltd Trading as Bramwell Property Finders, a company registered in England &amp; Wales, No.7351926 Registered office: 41 Hollinmoor Court, Hollinmoor Road, London, SW9 3PL</div>
    </footer>
    <div class="letterhead__footer-rule"></div>
  </section>

  <section class="card card--front">
    <div class="card__motif" role="img" aria-label="Faint magnifying glass outline motif"></div>
    <span class="wordmark">Bramwell Property Finders</span>
  </section>

  <section class="card card--back">
    <div class="card__motif" role="img" aria-label="Faint magnifying glass outline motif"></div>
    <div class="card__details">
      <div class="card__name">Owen Bramwell</div>
      <div class="card__line"><span class="label">T:</span> 0208 394 2860<span class="sep">|</span><span class="label">M:</span> +44(0)7932 418 507</div>
      <div class="card__line"><span class="label">E:</span> info@bramwellpropertyfinders.co.uk</div>
      <div class="card__line card__line--web"><span class="label">W:</span> bramwellpropertyfinders.co.uk</div>
    </div>
    <div class="card__rule"></div>
    <div class="card__tagline">London Property Finders and Search Agents</div>
  </section>

</div>
</body>
</html>
```